Flyer-Design für Motorradbranche
Zielgruppe
Wir sind in der Motorradbranche tätig .
Unser Producktportfoglio erstreckt sich von Motorräder über Motorradbekleidung, bis hinzu Events und spezielle Umbauten.
Unsere Zielgruppe ist sehr breit .
Alter: 16-70 Jahre
Da wir Premium-Produkte verkaufen erwarten unsere Kunden gute Qualität.
Aufgabenstellung
Dieser Flyer sollte etwas frischer gestaltet werden und moderner wirken. Dies ist ein Falzflyer, er wird in 3 gleichgrosse teile gefaltet. Das ganze ist eine Mischung zwischen einem Gutschein und einem Flyer der verteilt wird.
Information die enthalten sein müssen:
- Preis: 370 Euro
- Rabat: 30 Euro
- Datum: 20 April & 17 August 2018
Ansonsten ist alles gleich wie auf dem alten Flyer
Auf unserer Webseite ist der Event wie folgt ausgeschrieben:
https://www.rad-kessler.ch/de/events/feel+the+ride+-+in+piste+de+verlon/582
Format: 301 x 214mm
Das Kessler Tour logo sollte verwendet werden.
Wir sind gespannt was euch so einfällt.

```html
<!DOCTYPE html>
<html lang="de">
<head>
<meta charset="utf-8">
<title>Feel the Ride – Falzflyer</title>
<link href="https://fonts.googleapis.com/css2?family=Racing+Sans+One&family=Jost:wght@400;500;600&display=swap" rel="stylesheet">
<style>
  :root {
    --stage: #9a9a9a;
    --paper: #f2f2f2;
    --paper-shade: #c9c9c9;
    --ink: #2b2b2b;
    --ink-soft: #4a4a4a;
    --accent: #e0313d;
    --headline-grey: #5a5a5a;
  }
  * { margin: 0; padding: 0; box-sizing: border-box; }
  html, body { width: 1200px; height: 907px; overflow: hidden; }
  body { background: var(--stage); font-family: "Jost", sans-serif; color: var(--ink); }

  .flyer {
    position: absolute; left: 30px; top: 48px;
    width: 1140px; height: 811px;
    display: grid; grid-template-columns: repeat(3, 380px);
    box-shadow: 0 10px 30px rgba(0,0,0,.25);
  }
  .panel { position: relative; overflow: hidden; }

  /* Innenseite links */
  .panel--intro {
    background: linear-gradient(160deg, #d6d6d6 0%, #e4e4e4 45%, var(--paper-shade) 100%);
    padding: 70px 34px 0 40px; text-align: center;
  }
  .intro-title {
    font-family: "Racing Sans One", sans-serif; font-size: 30px; line-height: 1.05;
    text-transform: uppercase; color: var(--ink); margin-bottom: 26px;
  }
  .intro-text { font-size: 17px; line-height: 1.3; color: var(--ink); margin-bottom: 16px; }
  .intro-welcome { position: absolute; left: 40px; right: 34px; top: 470px; font-size: 17px; line-height: 1.3; }
  .intro-signoff {
    position: absolute; left: 40px; right: 34px; top: 620px;
    font-size: 24px; font-weight: 600; line-height: 1.2; color: var(--ink);
  }

  /* Bildleiste Mitte */
  .panel--gallery { display: grid; grid-template-rows: 205px 200px 200px 206px; }
  .photo--race { background: linear-gradient(135deg, #6f8f55 0%, #8a8f8a 40%, #5d6166 100%); }
  .photo--group { background: linear-gradient(180deg, #7fa3c8 0%, #5a7d48 35%, #3a3d44 100%); }
  .photo--track { background: linear-gradient(180deg, #3e4a3a 0%, #5f7a45 45%, #8d9296 100%); }
  .photo--riders { background: linear-gradient(180deg, #8aa7c9 0%, #5b6066 55%, #2f3135 100%); }

  /* Titelseite rechts */
  .panel--cover { background: linear-gradient(180deg, #ffffff 0%, var(--paper) 100%); text-align: center; padding-top: 100px; }
  .brand { display: flex; align-items: center; justify-content: center; gap: 10px; margin-bottom: 22px; }
  .brand-dot { width: 30px; height: 30px; border-radius: 50%; border: 3px solid var(--accent); }
  .brand-name { font-family: "Jost", sans-serif; font-weight: 600; font-size: 24px; color: var(--accent); text-transform: uppercase; letter-spacing: 1px; }
  .cover-title { font-family: "Racing Sans One", sans-serif; font-size: 40px; line-height: 1.1; color: var(--headline-grey); text-transform: uppercase; letter-spacing: 1px; }
  .cover-tagline { font-family: "Racing Sans One", sans-serif; font-size: 17px; line-height: 1.15; text-transform: uppercase; color: var(--ink-soft); margin-top: 12px; }
  .cover-tagline .hl { color: var(--accent); }
  .bike-art { display: block; margin: 26px auto 0; width: 300px; height: 150px; border-radius: 6px; background: linear-gradient(90deg, rgba(43,43,43,0) 0%, #3a3a3a 45%, #2b2b2b 100%); }
  .cover-date { font-family: "Racing Sans One", sans-serif; font-size: 22px; line-height: 1.15; text-transform: uppercase; color: var(--ink); margin-top: 24px; }
  .cover-copy { font-size: 18px; line-height: 1.3; color: var(--ink-soft); margin-top: 14px; }
  .cover-price { font-family: "Racing Sans One", sans-serif; font-size: 20px; line-height: 1.2; text-transform: uppercase; color: var(--ink); margin-top: 16px; }
  .cover-price .hl { color: var(--accent); }
</style>
</head>
<body>
  <main class="flyer">
    <section class="panel panel--intro">
      <h2 class="intro-title">Lernen mit Freude<br>macht sicher</h2>
      <p class="intro-text">Um die grösstmögliche Sicherheit zu erhalten und sein Motorrad ohne Ablenkung zu entdecken, werden die Kurse auf der nahen und abgesperrten Piste de Verlon durchgeführt.</p>
      <p class="intro-text">Ca. 1 ½ Stunden ab Zürich oder Bern</p>
      <p class="intro-welcome">Wir freuen uns euch auf dem Ring zu begrüssen und mit euch einen tollen Tag mit viel Spass zu verbringen.</p>
      <p class="intro-signoff">Euer<br>FEEL THE RIDE TEAM</p>
    </section>

    <section class="panel panel--gallery">
      <div class="photo photo--race" role="img" aria-label="Foto: Motorradfahrer in Schräglage auf der Rennstrecke"></div>
      <div class="photo photo--group" role="img" aria-label="Foto: Gruppenbild der Teilnehmenden vor einem Banner"></div>
      <div class="photo photo--track" role="img" aria-label="Foto: Motorräder auf der Piste zwischen Bäumen"></div>
      <div class="photo photo--riders" role="img" aria-label="Foto: Teilnehmende mit Reiseenduros jubeln an der Strecke"></div>
    </section>

    <section class="panel panel--cover">
      <div class="brand">
        <span class="brand-dot"></span>
        <span class="brand-name">Kessler Tour</span>
      </div>
      <h1 class="cover-title">Feel the Ride</h1>
      <p class="cover-tagline"><span class="hl">Feel</span> - Fühlen<br><span class="hl">the Ride</span> - die Fahrt</p>
      <div class="bike-art" role="img" aria-label="Illustration: Silhouette eines Motorrads mit Fahrtlinien"></div>
      <p class="cover-date">20 April &amp; 17 August 2018<br>in Piste de Verlon</p>
      <p class="cover-copy">Der 3-stuffige Motorradkurs<br>für besseres Fahren!</p>
      <p class="cover-copy">Mit viel Spass mehr<br>Sicherheit!</p>
      <p class="cover-price">Preis 370 Euro – <span class="hl">30 Euro Rabatt</span></p>
    </section>
  </main>
</body>
</html>
```